KORBALT

The business want a professional looking business card. We have a scetch we will add but want the extra upgrade, and would like more suggestions for variations of our business cards.

```html
<!DOCTYPE html>
<html lang="en">
<head>
<meta charset="utf-8">
<title>KORBALT business card</title>
<link rel="stylesheet" href="https://fonts.googleapis.com/css2?family=Arimo:wght@400;500&display=swap">
<style>
  :root {
    --backdrop: #3d3d3d;
    --card: #ffffff;
    --gold: #b88c45;
    --gold-deep: #6f4e25;
    --gold-mid: #b38a48;
    --gold-light: #ecc370;
    --ink: #55565a;
    --white: #ffffff;
  }
  * { margin: 0; padding: 0; box-sizing: border-box; }
  html, body {
    width: 1200px; height: 1200px; overflow: hidden;
    background: var(--backdrop);
    font-family: "Arimo", Arial, sans-serif;
  }
  .stage { position: relative; width: 1200px; height: 1200px; }
  .card {
    position: absolute;
    width: 693px; height: 396px;
    background: var(--card);
    border-radius: 26px;
    overflow: hidden;
    box-shadow: 0 4px 14px rgba(0,0,0,0.35);
  }
  .card--front { left: 268px; top: 159px; }
  .card--back  { left: 264px; top: 657px; }

  .brand {
    position: absolute;
    display: flex; align-items: center; gap: 10px;
    color: var(--gold);
    font-weight: 500;
    letter-spacing: 0.22em;
    white-space: nowrap;
  }
  .brand__dot {
    display: block; border-radius: 50%;
    background: var(--gold);
  }
  .card--front .brand {
    left: 226px; top: 225px; transform: translate(-50%, -50%);
    font-size: 27px;
  }
  .card--front .brand__dot { width: 14px; height: 14px; }
  .card--back .brand {
    left: 346px; top: 190px; transform: translate(-50%, -50%);
    font-size: 36px; gap: 14px;
  }
  .card--back .brand__dot { width: 18px; height: 18px; }

  .person { position: absolute; left: 387px; top: 126px; }
  .person__name { color: var(--gold); font-size: 21px; line-height: 1.2; }
  .person__role { color: var(--ink); font-size: 15.5px; margin-top: 4px; }

  .contacts { position: absolute; left: 387px; top: 206px; list-style: none; }
  .contacts li {
    display: flex; align-items: center; gap: 9px;
    color: var(--ink); font-size: 16px; line-height: 21px;
  }
  .contacts svg { width: 11px; height: 11px; flex: none; }

  .web-band {
    position: absolute; left: 0; top: 326px;
    width: 100%; height: 35px;
    background: linear-gradient(90deg, var(--gold-deep) 0%, var(--gold-mid) 55%, var(--gold-light) 85%, var(--gold-light) 100%);
  }
  .web-band__url {
    position: absolute; left: 312px; top: 50%;
    transform: translate(-50%, -50%);
    color: var(--white); font-size: 15px; letter-spacing: 0.14em;
  }
  .web-band__mark {
    position: absolute; left: 557px; top: 50%;
    width: 22px; height: 22px; transform: translateY(-50%);
    border: 2px solid var(--white); border-radius: 50%;
  }
</style>
</head>
<body>
<main class="stage">
  <section class="card card--front" aria-label="Card front">
    <div class="brand"><span class="brand__dot"></span>KORBALT</div>

    <div class="person">
      <p class="person__name">Lars Henrik Solvang</p>
      <p class="person__role">CEO &amp; Founder</p>
    </div>

    <ul class="contacts">
      <li>
        <svg viewBox="0 0 11 11" aria-hidden="true"><rect x="2.5" y="0.5" width="6" height="10" rx="1" fill="none" stroke="#b88c45" stroke-width="1.2"/></svg>
        004791234567
      </li>
      <li>
        <svg viewBox="0 0 11 11" aria-hidden="true"><rect x="0.5" y="2" width="10" height="7" fill="#b88c45"/><path d="M0.5 2 L5.5 6 L10.5 2" fill="none" stroke="#fff" stroke-width="1"/></svg>
        korbalt.llc@mailbox.com
      </li>
    </ul>

    <div class="web-band">
      <span class="web-band__url">www.korbalt.llc</span>
      <span class="web-band__mark"></span>
    </div>
  </section>

  <section class="card card--back" aria-label="Card back">
    <div class="brand"><span class="brand__dot"></span>KORBALT</div>
  </section>
</main>
</body>
</html>
```